Natural Australian skin care company packaging for new product Bath salts

We are moving to fully refillable packaging and need someone to design our refill pouches. we have a number of products we need to do this for but our first one is our natural bath salts. This comes in a 200g tin in a pouch then the pouch can be bought to refill the tin. We can either print on the pouch or do sickers. The tin is a simple matt black tin with white text on the lid. the pouch comes in a gold colour. pictures are in the drop box lid.
Luxury bath salts Pouch - the dimensions are 60*55*180mm, , we can either print directly or do a sticker, We also need the sleeve to go around the tin. The dimensions of the tin are 65x65x70mm. The same text needs to go onto the sleeve as the pouch. The tin is black with white printing on the top (see picture).
Text is as follows
VT logo Quiet moss tide 100% pure magnesium bath salts
A rich fragrance of Australian wild flowers (using natural essential oils) with frangipani and gardenia. Sink into the natural ancient salt lake sourced 100% pure magnesium to replenish your skin. Transdermal absorption of magnesium is effective and contributes to electrolyte balance, normal muscle function and aids calcium absorption. The ultimate mineral reset.
Directions: Fill bath, once full put two heaped tablespoons of the salts into the bath (approx 50g). Climb in and relax.
Vell Tonic full logo
Country of Origin: Australia
PO Box 318
Kelbrin Shore 4862
QLD Australia
www.velltonic.com
ingredients:
magnesium chloride *, parfum **
*naturally sourced from ancient salt lakes
**a combination of essential oils and natural isolates.
e: 200g / 7.05 Oz
We also need the recycle, plastic free, not tested on animal eco friendly symbols.
Please use this link to our press assets and tin and pouch photos.
https://www.filevaultra.com/sh/kq3p81wmxt02hd5/QXtrNbLm__kwLzPeYd-HsnqWjLa?dl=0

```html
<!DOCTYPE html>
<html lang="en">
<head>
<meta charset="utf-8">
<title>Vell Tonic – Bath Salts Refill Pouch Labels</title>
<link rel="stylesheet" href="https://fonts.googleapis.com/css2?family=Bitter:wght@700&family=Permanent+Marker&family=Quicksand:wght@500;600&family=Oswald:wght@300;400&display=swap">
<style>
  :root {
    --page: #ffffff;
    --pouch: #3fd3cc;
    --pouch-dark: #2fbdb6;
    --pouch-fold: #4fdcd5;
    --tab: #8fdcd8;
    --label: #a3ebe8;
    --label-clear: #b8f0ee;
    --ink: #111111;
    --teal-ink: #1c8f8a;
    --band: #237f7b;
    --red: #ed1c24;
    --white: #ffffff;
    --flower-leaf: #8fbf6a;
    --flower-petal: #8fb4e3;
    --salt: #c6f3f1;
    --dash: #8a8a8a;
  }
  * { box-sizing: border-box; margin: 0; padding: 0; }
  html, body { width: 675px; height: 1200px; overflow: hidden; background: var(--page); }
  .board { position: relative; width: 675px; height: 1200px; }

  .tag {
    position: absolute; background: var(--red); color: var(--white);
    font-family: "Permanent Marker", cursive; text-align: center;
    display: flex; align-items: center; justify-content: center;
    font-size: 19px; line-height: 1.05; letter-spacing: 0.5px;
  }
  .tag--opaque { left: 325px; top: 136px; width: 303px; height: 63px; }
  .tag--clear { left: 354px; top: 581px; width: 242px; height: 63px; }

  /* pouch */
  .pouch {
    position: absolute; width: 204px; height: 303px;
    background: linear-gradient(90deg, var(--pouch-dark) 0%, var(--pouch) 12%, var(--pouch) 88%, var(--pouch-dark) 100%);
  }
  .pouch--top { left: 51px; top: 216px; }
  .pouch--bottom { left: 51px; top: 656px; }
  .pouch__fold { position: absolute; left: 0; top: 0; width: 100%; height: 27px; background: var(--pouch-fold); border-bottom: 1px solid var(--pouch-dark); }
  .pouch__seal {
    position: absolute; left: 76px; top: 0; width: 51px; height: 78px;
    background: var(--tab); border-radius: 0 0 26px 26px;
  }
  .seal__mark {
    position: absolute; left: 5px; top: 37px; width: 41px; height: 41px;
    border: 1.5px solid #2b6d6a; border-radius: 50%;
    display: flex; align-items: center; justify-content: center;
    font-family: "Bitter", serif; font-weight: 700; font-size: 15px; color: #2b6d6a;
  }
  .pouch__label {
    position: absolute; left: 23px; top: 108px; width: 260px; height: 287px;
    transform: scale(0.612); transform-origin: 0 0;
  }

  /* label */
  .label { position: absolute; width: 260px; height: 287px; text-align: center; }
  .label--opaque { background: var(--label); border-radius: 12px; overflow: hidden; }
  .label--clear-on-pouch { background: var(--label-clear); border-radius: 12px; overflow: hidden; }
  .sticker--opaque { left: 350px; top: 216px; }
  .sticker--clear { left: 349px; top: 661px; border: 1.2px dashed var(--dash); border-radius: 10px; }

  .label__brand { position: absolute; left: 0; right: 0; top: 20px; font-family: "Bitter", serif; font-weight: 700; font-size: 16px; letter-spacing: 0.4px; color: var(--ink); }
  .label__tagline { position: absolute; left: 0; right: 0; top: 41px; font-family: "Bitter", serif; font-weight: 700; font-size: 5px; letter-spacing: 0.3px; color: var(--ink); }
  .label__strength { position: absolute; left: 0; right: 0; top: 92px; font-family: "Quicksand", sans-serif; font-weight: 600; font-size: 12px; color: var(--ink); }
  .label__title { position: absolute; left: 0; right: 0; top: 105px; font-family: "Permanent Marker", cursive; font-size: 37px; line-height: 1; color: var(--ink); }
  .label__scent { position: absolute; left: 0; right: 0; top: 163px; font-family: "Quicksand", sans-serif; font-weight: 500; font-size: 15px; color: var(--teal-ink); }
  .label__band { position: absolute; left: 68px; top: 181px; width: 128px; height: 18px; }
  .label__oils { position: absolute; left: 68px; top: 184px; width: 128px; font-family: "Quicksand", sans-serif; font-weight: 600; font-size: 7.5px; color: var(--white); }
  .label__salt { position: absolute; left: 63px; top: 219px; width: 68px; height: 68px; border-radius: 50%; background: radial-gradient(circle, var(--salt) 0%, #a9ece9 100%); }
  .label__weight { position: absolute; left: 146px; top: 242px; text-align: left; font-family: "Oswald", sans-serif; font-weight: 300; font-size: 10px; line-height: 1.2; color: var(--ink); }

  .flora { position: absolute; background: linear-gradient(180deg, var(--flower-petal) 0%, #b9d7a6 45%, var(--flower-leaf) 100%); opacity: 0.8; border-radius: 40% 40% 6px 6px; }
  .label--opaque .flora--left, .label--clear-on-pouch .flora--left { left: 0; top: 170px; width: 58px; height: 117px; }
  .label--opaque .flora--right, .label--clear-on-pouch .flora--right { left: 190px; top: 120px; width: 70px; height: 167px; }
  .sticker--clear .flora--left { left: -62px; top: 170px; width: 113px; height: 174px; }
  .sticker--clear .flora--right { left: 185px; top: 114px; width: 125px; height: 231px; }
</style>
</head>
<body>
<main class="board">

  <section class="pouch pouch--top" aria-label="Refill pouch with opaque label">
    <div class="pouch__fold"></div>
    <div class="pouch__seal"><div class="seal__mark">VT</div></div>
    <div class="pouch__label">
      <div class="label label--opaque">
        <div class="flora flora--left" role="img" aria-label="Forget-me-not flower illustration"></div>
        <div class="flora flora--right" role="img" aria-label="Forget-me-not flower illustration"></div>
        <div class="label__brand">VELL TONIC</div>
        <div class="label__tagline">AUSTRALIAN NATURAL SKINCARE</div>
        <div class="label__strength">100% pure magnesium</div>
        <div class="label__title">BATH SALTS</div>
        <div class="label__scent">Scentname</div>
        <svg class="label__band" viewBox="0 0 128 18" aria-hidden="true"><path d="M2 4 Q40 1 126 3 L122 9 L127 15 Q60 17 4 16 L0 10 Z" fill="var(--band)"/></svg>
        <div class="label__oils">with natural essential oils</div>
        <div class="label__salt" role="img" aria-label="Pile of bath salt crystals"></div>
        <div class="label__weight">NET WT<br>7.05 OZ. (200g) &nbsp;℮</div>
      </div>
    </div>
  </section>

  <div class="tag tag--opaque">NON-TRANSPARENT<br>STICKER</div>

  <div class="label label--opaque sticker--opaque">
    <div class="flora flora--left" role="img" aria-label="Forget-me-not flower illustration"></div>
    <div class="flora flora--right" role="img" aria-label="Forget-me-not flower illustration"></div>
    <div class="label__brand">VELL TONIC</div>
    <div class="label__tagline">AUSTRALIAN NATURAL SKINCARE</div>
    <div class="label__strength">100% pure magnesium</div>
    <div class="label__title">BATH SALTS</div>
    <div class="label__scent">Scentname</div>
    <svg class="label__band" viewBox="0 0 128 18" aria-hidden="true"><path d="M2 4 Q40 1 126 3 L122 9 L127 15 Q60 17 4 16 L0 10 Z" fill="var(--band)"/></svg>
    <div class="label__oils">with natural essential oils</div>
    <div class="label__salt" role="img" aria-label="Pile of bath salt crystals"></div>
    <div class="label__weight">NET WT<br>7.05 OZ. (200g) &nbsp;℮</div>
  </div>

  <section class="pouch pouch--bottom" aria-label="Refill pouch with transparent label">
    <div class="pouch__fold"></div>
    <div class="pouch__seal"><div class="seal__mark">VT</div></div>
    <div class="pouch__label">
      <div class="label label--clear-on-pouch">
        <div class="flora flora--left" role="img" aria-label="Forget-me-not flower illustration"></div>
        <div class="flora flora--right" role="img" aria-label="Forget-me-not flower illustration"></div>
        <div class="label__brand">VELL TONIC</div>
        <div class="label__tagline">AUSTRALIAN NATURAL SKINCARE</div>
        <div class="label__strength">100% pure magnesium</div>
        <div class="label__title">BATH SALTS</div>
        <div class="label__scent">Scentname</div>
        <svg class="label__band" viewBox="0 0 128 18" aria-hidden="true"><path d="M2 4 Q40 1 126 3 L122 9 L127 15 Q60 17 4 16 L0 10 Z" fill="var(--band)"/></svg>
        <div class="label__oils">with natural essential oils</div>
        <div class="label__salt" role="img" aria-label="Pile of bath salt crystals"></div>
        <div class="label__weight">NET WT<br>7.05 OZ. (200g) &nbsp;℮</div>
      </div>
    </div>
  </section>

  <div class="tag tag--clear">TRANSPARENT STICKER</div>

  <div class="label sticker--clear">
    <div class="flora flora--left" role="img" aria-label="Forget-me-not flower illustration"></div>
    <div class="flora flora--right" role="img" aria-label="Forget-me-not flower illustration"></div>
    <div class="label__brand">VELL TONIC</div>
    <div class="label__tagline">AUSTRALIAN NATURAL SKINCARE</div>
    <div class="label__strength">100% pure magnesium</div>
    <div class="label__title">BATH SALTS</div>
    <div class="label__scent">Scentname</div>
    <svg class="label__band" viewBox="0 0 128 18" aria-hidden="true"><path d="M2 4 Q40 1 126 3 L122 9 L127 15 Q60 17 4 16 L0 10 Z" fill="var(--band)"/></svg>
    <div class="label__oils">with natural essential oils</div>
    <div class="label__salt" role="img" aria-label="Pile of bath salt crystals"></div>
    <div class="label__weight">NET WT<br>7.05 OZ. (200g) &nbsp;℮</div>
  </div>

</main>
</body>
</html>
```